UPDATE: I have uploaded the selected logo from the other contest, please use it in your designs.

I have a logo design contest as well so not sure how ArtHive handles that. They should integrate at some point. I will describe the overall theme with the logo description. See it for details.

The business card side of it would just build on that same theme.

Target Market(s)

8-40

Industry/Entity Type

Business

Contact Information for Business Card

FirstName LastName
Email

Logo Text

VelMarin

Font styles to use
Sans Serif

Requirements
Must have
• the url VelMarin.com somewhere in it.

```html
<!DOCTYPE html>
<html lang="en">
<head>
<meta charset="utf-8">
<title>VelMarin Business Card</title>
<link href="https://fonts.googleapis.com/css2?family=Lato:wght@300;400;700;900&display=swap" rel="stylesheet">
<style>
  :root {
    --backdrop: #e4e6e9;
    --card-white: #ffffff;
    --brand-blue: #1670b8;
    --brand-ink: #1670b8;
    --text-light: #ffffff;
    --card-shadow: rgba(20, 30, 45, 0.22);
  }
  * { margin: 0; padding: 0; box-sizing: border-box; }
  html, body {
    width: 1200px;
    height: 926px;
    overflow: hidden;
    background: var(--backdrop);
    font-family: "Lato", sans-serif;
  }
  .sheet {
    width: 1200px;
    height: 926px;
    display: flex;
    flex-direction: column;
    align-items: center;
    justify-content: center;
    gap: 46px;
  }
  .card {
    width: 700px;
    height: 400px;
    border-radius: 4px;
    box-shadow: 0 10px 28px var(--card-shadow);
    display: flex;
    flex-direction: column;
    align-items: center;
    justify-content: center;
  }
  .card--front { background: var(--card-white); }
  .card--back { background: var(--brand-blue); color: var(--text-light); }

  .wordmark {
    display: flex;
    align-items: center;
    gap: 16px;
  }
  .wordmark__dot {
    width: 22px;
    height: 22px;
    border-radius: 50%;
  }
  .wordmark__name {
    font-weight: 900;
    font-size: 64px;
    letter-spacing: 10px;
    text-transform: uppercase;
    line-height: 1;
  }
  .card--front .wordmark__dot { background: var(--brand-ink); }
  .card--front .wordmark__name { color: var(--brand-ink); }
  .card--back .wordmark__dot { background: var(--text-light); }
  .card--back .wordmark__name { color: var(--text-light); font-size: 50px; letter-spacing: 8px; }

  .contact {
    margin-top: 30px;
    text-align: center;
  }
  .contact__name {
    font-size: 38px;
    font-weight: 300;
    letter-spacing: 1px;
    line-height: 1.1;
  }
  .contact__name strong { font-weight: 700; }
  .contact__line {
    font-size: 21px;
    font-weight: 400;
    letter-spacing: 1px;
    margin-top: 6px;
  }
</style>
</head>
<body>
  <main class="sheet">
    <section class="card card--front" aria-label="Card front">
      <div class="wordmark">
        <span class="wordmark__dot"></span>
        <span class="wordmark__name">VelMarin</span>
      </div>
    </section>

    <section class="card card--back" aria-label="Card back">
      <div class="wordmark">
        <span class="wordmark__dot"></span>
        <span class="wordmark__name">VelMarin</span>
      </div>
      <div class="contact">
        <p class="contact__name">ALEX <strong>ROWAN</strong></p>
        <p class="contact__line">VelMarin.com</p>
        <p class="contact__line">alexrowan@VelMarin.com</p>
      </div>
    </section>
  </main>
</body>
</html>
```